Letterhead PT. Bima Raya Lestari Developer

Alo , My Company need a letterhead design for PT. Bima Raya Lestari Developer Real Estate , i need your each other creative design letterhead for my PT.Bima Raya Lestari Developer Real Estate guys
input my data in letterhead :
Address : Komp. Ruko Taman Sari Blok F No. 27
No. Telp : 0778 512 3364 / 0812 4395 7716
Email : bimarayalestari@mailbox-example.com
Website : www.bimarayalestari-example.com

Target Market(s)

Buyer Property Real Estate & Investor

Industry/Entity Type

Real Estate Development

Font styles to use
Serif
Sans Serif

Requirements
Must have
• according to your creative each other guys as long i need
• Address : Komp. Ruko Taman Sari Blok F No. 27
• No. Telp : 0778 512 3364 / 0812 4395 7716
• Email : bimarayalestari@mailbox-example.com
• Website : www.bimarayalestari-example.com
Nice to have
Should not have
• don't want another colour except : white , dark blue n gold suit to our logo developer real estate

```html
<!DOCTYPE html>
<html lang="en">
<head>
<meta charset="utf-8">
<title>Letterhead – PT. Bima Raya Lestari Developer</title>
<link rel="stylesheet" href="https://fonts.googleapis.com/css2?family=EB+Garamond:wght@400&family=Montserrat:wght@600&display=swap">
<style>
  :root {
    --backdrop: #e7e3db;
    --paper: #f8f7ef;
    --navy: #33597d;
    --navy-deep: #2e5475;
    --ink: #2b2b2b;
    --gold-gradient: linear-gradient(180deg, #b88d52 0%, #dcc39a 22%, #f3e9d6 42%, #fbf7ee 55%, #e3cca3 75%, #b9904f 100%);
  }
  * { box-sizing: border-box; margin: 0; padding: 0; }
  html, body { width: 1200px; height: 1200px; overflow: hidden; background: var(--backdrop); }
  .letterhead {
    position: absolute; left: 174px; top: 50px;
    width: 852px; height: 1100px;
    background: var(--paper);
    box-shadow: 0 6px 24px rgba(0,0,0,.18);
    font-family: "EB Garamond", Georgia, serif;
    color: var(--ink);
    overflow: hidden;
  }
  .top-band { position: absolute; left: 0; top: 0; width: 100%; height: 19px; background: var(--navy); }
  .top-gold {
    position: absolute; left: 410px; top: 19px; width: 442px; height: 89px;
    background: var(--gold-gradient);
    clip-path: polygon(0 0, 100% 0, 100% 100%, 59px 100%);
  }
  .brand {
    position: absolute; left: 40px; top: 62px; width: 260px;
    text-align: center;
    font-family: "Montserrat", Arial, sans-serif; font-weight: 600;
    color: var(--navy); font-size: 17px; line-height: 1.25; letter-spacing: .3px;
  }
  .brand .mark { display: block; width: 34px; height: 34px; margin: 0 auto 8px; border-radius: 50%; background: var(--navy); }
  .recipient { position: absolute; left: 76px; top: 176px; font-size: 16px; line-height: 30px; letter-spacing: .3px; }
  .body { position: absolute; left: 75px; top: 321px; width: 700px; font-size: 15.6px; line-height: 30.2px; }
  .body p { text-align: justify; text-indent: 40px; hyphens: auto; margin-bottom: 30px; }
  .signoff { position: absolute; left: 75px; top: 753px; font-size: 16px; line-height: 30px; letter-spacing: .3px; }
  .footer-rule { position: absolute; left: 81px; top: 904px; width: 690px; height: 6px; background: var(--navy); }
  .contact { position: absolute; display: flex; align-items: center; gap: 9px; font-size: 17.5px; letter-spacing: .2px; color: #333; }
  .contact svg { width: 17px; height: 17px; fill: #222; flex: none; }
  .contact.address { left: 100px; top: 939px; }
  .contact.phone { left: 100px; top: 973px; }
  .contact.email { left: 498px; top: 939px; font-size: 16.5px; }
  .contact.web { left: 498px; top: 973px; font-size: 16.5px; }
  .bottom-gold {
    position: absolute; left: 78px; top: 1027px; width: 464px; height: 73px;
    background: var(--gold-gradient);
    clip-path: polygon(0 0, 100% 0, 100% 100%, 49px 100%);
  }
  .bottom-navy { position: absolute; left: 542px; top: 1027px; width: 310px; height: 73px; background: var(--navy-deep); }
</style>
</head>
<body>
  <main class="letterhead">
    <div class="top-band"></div>
    <div class="top-gold"></div>

    <div class="brand">
      <span class="mark"></span>
      PT. BIMA RAYA LESTARI<br>DEVELOPER
    </div>

    <address class="recipient" style="font-style:normal">
      21 Cedar St. Rd.4<br>
      Harlow City<br>
      Westbrook, 40519
    </address>

    <section class="body">
      <p>Lorem Ipsum has been the industry's standard dummy text ever since the 1500s, when an unknown printer took a galley of type and scrambled it to make a type specimen book. It has survived not only five centuries, but also the leap into electronic typesetting, remaining essentially unchanged. It was popularised in the 1960s with the release of Letterline sheets containing Lorem Ipsum passages, and more recently with desktop publishing software like Pagecraft Layout including versions of Lorem Ipsum.</p>
      <p>Lorem Ipsum has been the industry's standard dummy text ever since the 1500s, when an unknown printer took a galley of type and scrambled it to make a type specimen book. It has survived not only five centuries, but also the leap into electronic typesetting, remaining essentially unchanged. It was popularised in the 1960s with the release of Letterline sheets containing Lorem Ipsum passages, and more recently with desktop publishing software like Pagecraft Layout including versions of Lorem Ipsum.</p>
    </section>

    <div class="signoff">
      Sincerely,<br>
      Jane Doe<br>
      Executive Marketing
    </div>

    <div class="footer-rule"></div>

    <div class="contact address">
      <svg viewBox="0 0 24 24"><path d="M12 2a7 7 0 0 0-7 7c0 5.2 7 13 7 13s7-7.8 7-13a7 7 0 0 0-7-7zm0 9.5A2.5 2.5 0 1 1 12 6.5a2.5 2.5 0 0 1 0 5z"/></svg>
      <span>Komp. Ruko Taman Sari Blok F No. 27</span>
    </div>
    <div class="contact phone">
      <svg viewBox="0 0 24 24"><path d="M6.6 10.8a15.1 15.1 0 0 0 6.6 6.6l2.2-2.2a1 1 0 0 1 1-.25 11.4 11.4 0 0 0 3.6.57 1 1 0 0 1 1 1V20a1 1 0 0 1-1 1A17 17 0 0 1 3 4a1 1 0 0 1 1-1h3.5a1 1 0 0 1 1 1c0 1.25.2 2.45.57 3.6a1 1 0 0 1-.25 1z"/></svg>
      <span>0778 512 3364 / 0812 4395 7716</span>
    </div>
    <div class="contact email">
      <svg viewBox="0 0 24 24"><path d="M2 5h20v14H2zm2 2v.4l8 5.3 8-5.3V7zm0 2.8V17h16V9.8l-8 5.3z"/></svg>
      <span>bimarayalestari@mailbox-example.com</span>
    </div>
    <div class="contact web">
      <svg viewBox="0 0 24 24" fill="none" stroke="#222" stroke-width="1.8" style="fill:none"><circle cx="12" cy="12" r="9.5"/><ellipse cx="12" cy="12" rx="4.2" ry="9.5"/><path d="M2.5 12h19M4 7h16M4 17h16"/></svg>
      <span>www.bimarayalestari-example.com</span>
    </div>

    <div class="bottom-gold"></div>
    <div class="bottom-navy"></div>
  </main>
</body>
</html>
```